IRON SASH VIGOUR CERTIFICATE

Carrowby Hapkido Inc is wanting to introduce a fitness system based upon certificates reflecting rank; White - Yellow - Blue - Red - Black.

The Certificate "MUST" have on it "IRON SASH VIGOUR"

The Certificate "MUST" have a martial arts theme!

The Certificate "MUST" reflect the fitness requirements for each rank.

The colour scheme for each Certificate "MUST" reflect the belt rank

The Certificate must include at least one martial arts graphic / motif

The certificate must have the Carrowby HKD LOGO

We will need a certificate template that can be for all levels but reflect the rank and fitness level. The certificate can be either traditional or modern style but must reflect a martial art themes. The certificate must have the Carrowby Hapkido logo incorporated into the certificate with signature space for senior instructors Dan Pellow & Sorna Vick-Pellow. The certificates should be eye catching and exciting to look at. It should bold and incorporate martial art motifs etc The fitness requirements are not onerous and the certificate system is created to incentivise physical activity and correct technique rather than creating an impossible standards only Olympians can achieve. The majority of our students are upper primary and lower secondary from 11yr-15yrs. Certificate should be youthful but not silly. The certificate template will be reproduced for each colour belt.White = 10 push ups 10 Sit ups 10 squats 10 Jumping Jacks 20 sec plank 400m continuous run Demonstrate beginner stretching techniqueYellow = 20 push ups 20 sit ups 20 squats 20 Jumping Jacks 40 Sec plank 800m continuous run Demonstrate intermediate stretching techniqueBlue = 30 push ups 30 sit ups 30 squats 30 Jumping Jacks 60 Sec plank 1200m continuous run Demonstrate intermediate stretching techniqueRed = 40 push ups 40 sit ups 40 squats 40 Jumping Jacks 75sec plank 1600m run Demonstrate advanced stretching techniqueBlack = 50 push ups 50 sit ups 50 squats 50 Jumping jacks 90 sec planks 2000m continuous run Demonstrate advanced stretching technique
Updates

HI Designers, Please go for modern and professionals. Several designs have used traditional motifs of water dragons or lattice bordering. This looks old school. Please do not use martial art silhouettes as it looks amateur. Definately looking for upmarket high quality presentations.

Logo Text

IRON SASH VIGOUR

Font styles to use
Decorative

Colors

Designer to choose colors to be used in the design.

Requirements
Must have
• This will be a template foe all coloured ranks of fitness, Be bold, memorable, should be themed to martial arts etc

```html
<!DOCTYPE html>
<html lang="en">
<head>
<meta charset="utf-8">
<title>Iron Sash Vigour Certificate</title>
<link rel="stylesheet" href="https://fonts.googleapis.com/css2?family=Bebas+Neue&family=Oswald:wght@500&family=Montserrat:wght@500;600;700&family=Mulish:wght@700&display=swap">
<style>
  :root {
    --red: #ed1c24;
    --navy: #1d222c;
    --navy-light: #2c3442;
    --ink: #15181f;
    --paper: #ffffff;
    --watermark: #e6e6e6;
    --belt-white: #d9d9d9;
    --belt-yellow: #f2c200;
    --belt-red: #d8252b;
    --belt-blue: #1a5bb5;
    --belt-black: #141414;
  }
  * { margin: 0; padding: 0; box-sizing: border-box; }
  html, body { width: 921px; height: 1200px; overflow: hidden; background: var(--paper); }
  .certificate { position: relative; width: 921px; height: 1200px; background: var(--paper); overflow: hidden; }

  .header { position: absolute; left: 0; top: 0; width: 921px; height: 294px; background: linear-gradient(90deg, var(--navy) 0%, var(--navy-light) 60%, var(--navy) 100%); }
  .header__band { position: absolute; left: 24px; top: 0; width: 897px; height: 125px; background: var(--red); }
  .header__title { position: absolute; left: 268px; top: 24px; width: 630px; text-align: center; font-family: "Bebas Neue", sans-serif; font-weight: 400; font-size: 92px; line-height: 1; color: var(--paper); letter-spacing: 2px; white-space: nowrap; }
  .header__subtitle { position: absolute; left: 268px; top: 132px; width: 640px; font-family: "Bebas Neue", sans-serif; font-weight: 400; font-size: 158px; line-height: 1; color: var(--red); transform: skewX(-12deg); letter-spacing: 0; white-space: nowrap; text-align: center; }

  .brand { position: absolute; left: 26px; top: 30px; width: 226px; height: 226px; border-radius: 50%; background: var(--red); border: 10px solid var(--navy); display: flex; align-items: center; justify-content: center; text-align: center; }
  .brand__name { font-family: "Bebas Neue", sans-serif; font-size: 40px; line-height: 1.05; color: var(--paper); letter-spacing: 2px; }

  .intro { position: absolute; left: 39px; top: 318px; width: 850px; }
  .intro__lead { font-family: "Oswald", sans-serif; font-weight: 500; font-size: 42px; line-height: 1.1; color: var(--ink); white-space: nowrap; letter-spacing: -0.6px; }
  .intro__sub { margin-top: 2px; font-family: "Montserrat", sans-serif; font-weight: 700; font-size: 22.5px; color: var(--red); text-transform: uppercase; white-space: nowrap; }

  .watermark { position: absolute; left: 380px; top: 500px; width: 540px; height: 580px; background: radial-gradient(ellipse at 50% 45%, var(--watermark) 0%, rgba(230,230,230,0.6) 45%, rgba(255,255,255,0) 72%); }

  .ranks { position: absolute; left: 37px; top: 430px; width: 860px; list-style: none; }
  .rank { position: absolute; left: 0; display: flex; width: 860px; }
  .rank--white { top: 0; } .rank--yellow { top: 130px; } .rank--red { top: 261px; } .rank--blue { top: 406px; } .rank--black { top: 536px; }
  .rank--white { color: var(--belt-white); }
  .rank--yellow { color: var(--belt-yellow); }
  .rank--red { color: var(--belt-red); }
  .rank--blue { color: var(--belt-blue); }
  .rank--black { color: var(--belt-black); }
  .rank__belt { position: relative; width: 80px; height: 108px; flex: none; }
  .rank__belt svg { position: absolute; left: 0; top: 0; width: 80px; height: 108px; }
  .rank__tag { position: absolute; left: 0; top: 17px; width: 80px; font-family: "Montserrat", sans-serif; font-weight: 500; font-size: 9px; line-height: 1.15; color: var(--ink); text-align: center; }
  .rank__text { margin-left: 25px; margin-top: 5px; font-family: "Mulish", sans-serif; font-weight: 700; font-size: 18.5px; line-height: 24px; color: var(--ink); width: 740px; }

  .signatures { position: absolute; left: 0; top: 1118px; width: 921px; }
  .signature { position: absolute; top: 0; width: 217px; border-top: 2px solid var(--ink); text-align: center; padding-top: 9px; font-family: "Montserrat", sans-serif; color: var(--ink); }
  .signature--left { left: 209px; } .signature--right { left: 498px; }
  .signature__name { font-weight: 600; font-size: 17px; text-transform: uppercase; white-space: nowrap; }
  .signature__role { font-weight: 500; font-size: 12px; margin-top: 2px; }
</style>
</head>
<body>
<main class="certificate">
  <header class="header">
    <div class="header__band"></div>
    <div class="brand"><span class="brand__name">CARROWBY<br>HKD</span></div>
    <h1 class="header__title">IRON SASH VIGOUR</h1>
    <div class="header__subtitle">CERTIFICATE</div>
  </header>

  <section class="intro">
    <h2 class="intro__lead">CARROWBY HAPKIDO INC IS WANTING TO INTRODUCE</h2>
    <p class="intro__sub">A fitness system based upon certificates reflecting rank</p>
  </section>

  <div class="watermark" role="img" aria-label="Faint martial artist performing a high kick"></div>

  <ul class="ranks">
    <li class="rank rank--white">
      <div class="rank__belt" role="img" aria-label="White belt">
        <svg viewBox="0 0 80 108"><polygon points="30,62 14,104 28,108 40,70" fill="currentColor"/><polygon points="50,62 66,104 52,108 40,70" fill="currentColor"/><rect x="0" y="50" width="80" height="16" rx="3" fill="currentColor"/><rect x="31" y="48" width="18" height="20" rx="3" fill="currentColor" stroke="#fff" stroke-width="1.5"/><path d="M14 48 V22 A26 22 0 0 1 66 22 V48 Z" fill="#fff" stroke="currentColor" stroke-width="4"/></svg>
        <span class="rank__tag">WHITE<br>BELT</span>
      </div>
      <p class="rank__text">10 push ups 10 Sit ups 10 squats 10 Jumping Jacks 20 sec plank 400m continuous run.<br>Demonstrate beginner stretching technique.</p>
    </li>
    <li class="rank rank--yellow">
      <div class="rank__belt" role="img" aria-label="Yellow belt">
        <svg viewBox="0 0 80 108"><polygon points="30,62 14,104 28,108 40,70" fill="currentColor"/><polygon points="50,62 66,104 52,108 40,70" fill="currentColor"/><rect x="0" y="50" width="80" height="16" rx="3" fill="currentColor"/><rect x="31" y="48" width="18" height="20" rx="3" fill="currentColor" stroke="#fff" stroke-width="1.5"/><path d="M14 48 V22 A26 22 0 0 1 66 22 V48 Z" fill="#fff" stroke="currentColor" stroke-width="4"/></svg>
        <span class="rank__tag">YELLOW<br>BELT</span>
      </div>
      <p class="rank__text">20 push ups 20 sit ups 20 squats 20 Jumping Jacks 40 Sec plank 800m continuous run.<br>Demonstrate intermediate stretching technique.</p>
    </li>
    <li class="rank rank--red">
      <div class="rank__belt" role="img" aria-label="Red belt">
        <svg viewBox="0 0 80 108"><polygon points="30,62 14,104 28,108 40,70" fill="currentColor"/><polygon points="50,62 66,104 52,108 40,70" fill="currentColor"/><rect x="0" y="50" width="80" height="16" rx="3" fill="currentColor"/><rect x="31" y="48" width="18" height="20" rx="3" fill="currentColor" stroke="#fff" stroke-width="1.5"/><path d="M14 48 V22 A26 22 0 0 1 66 22 V48 Z" fill="#fff" stroke="currentColor" stroke-width="4"/></svg>
        <span class="rank__tag">RED<br>BELT</span>
      </div>
      <p class="rank__text">30 push ups 30 sit ups 30 squats 30 Jumping Jacks 60 Sec plank 1200m continuous run.<br>Demonstrate intermediate stretching technique.</p>
    </li>
    <li class="rank rank--blue">
      <div class="rank__belt" role="img" aria-label="Blue belt">
        <svg viewBox="0 0 80 108"><polygon points="30,62 14,104 28,108 40,70" fill="currentColor"/><polygon points="50,62 66,104 52,108 40,70" fill="currentColor"/><rect x="0" y="50" width="80" height="16" rx="3" fill="currentColor"/><rect x="31" y="48" width="18" height="20" rx="3" fill="currentColor" stroke="#fff" stroke-width="1.5"/><path d="M14 48 V22 A26 22 0 0 1 66 22 V48 Z" fill="#fff" stroke="currentColor" stroke-width="4"/></svg>
        <span class="rank__tag">BLUE<br>BELT</span>
      </div>
      <p class="rank__text">40 push ups 40 sit ups 40 squats 40 Jumping Jacks 75sec plank 1600m run<br>Demonstrate advanced stretching technique.</p>
    </li>
    <li class="rank rank--black">
      <div class="rank__belt" role="img" aria-label="Black belt">
        <svg viewBox="0 0 80 108"><polygon points="30,62 14,104 28,108 40,70" fill="currentColor"/><polygon points="50,62 66,104 52,108 40,70" fill="currentColor"/><rect x="0" y="50" width="80" height="16" rx="3" fill="currentColor"/><rect x="31" y="48" width="18" height="20" rx="3" fill="currentColor" stroke="#fff" stroke-width="1.5"/><path d="M14 48 V22 A26 22 0 0 1 66 22 V48 Z" fill="#fff" stroke="currentColor" stroke-width="4"/></svg>
        <span class="rank__tag">BLACK<br>BELT</span>
      </div>
      <p class="rank__text">50 push ups 50 sit ups 50 squats 50 Jumping jacks 90 sec planks 2000m continuous run.<br>Demonstrate advanced stretching technique.</p>
    </li>
  </ul>

  <footer class="signatures">
    <div class="signature signature--left">
      <p class="signature__name">Dan Pellow</p>
      <p class="signature__role">( senior instructors )</p>
    </div>
    <div class="signature signature--right">
      <p class="signature__name">Sorna Vick-Pellow</p>
      <p class="signature__role">( senior instructors )</p>
    </div>
  </footer>
</main>
</body>
</html>
```